Bold, dynamic Brick paver/landscaping company flyer

I need a flyer of 11" long x 8.5" high advertising our brick paver installation service. I want it clean, elegant and bold. I tried to give a general idea of what i was looking for by creating a very poor version for you guys to begin with. That being said, i am no designer, which is why i need your help. You have complete artistic license, show me what you got! I will attach our logo, the photos i used in the mock up as well as the mock up of basic idea. I hate my fonts, i hate to colors of them, i hate the way the pictures overlap without any seperation, but i like the basic idea. Use your artistic vision and skill to transform into something with a flair that will leave my potential customers thinking i am the most upscale service in the area. Please dont hesitate to ask any questions.

all of this bieng said, if you have an awesome idea thats completely different, im not invested in this idea alone, i will consider all options equally. Thanks!

Target Market(s)

high end homes, wealthy clientle

Industry/Entity Type

Advertising

Requirements
Must have
• Must have the blank white box in the upper right corner of approximate size, doesnt have to be exact. the gopher should be removed as well. The text "local postal customer should be there at the bottom of the box.

Company Name, phone number and web address

I like the wording of the text in the upper left, but hate the look of it

```html
<!DOCTYPE html>
<html lang="en">
<head>
<meta charset="utf-8">
<title>Evergreen Crest Landscaping – Paver Flyer</title>
<link rel="stylesheet" href="https://fonts.googleapis.com/css2?family=Arimo:ital,wght@0,400;0,700;1,400;1,700&display=swap">
<style>
  :root {
    --page-bg: #e4e4e1;
    --leaf-pale: #eef5d2;
    --leaf-light: #cfe28e;
    --leaf-mid: #9cc43f;
    --leaf-lime: #c6e04a;
    --leaf-deep: #6f9a22;
    --leaf-dark: #4f7a17;
    --ink-green: #2f5a10;
    --ink-dark: #23330f;
    --paper: #ffffff;
    --card: #f1f7dc;
  }
  * { margin: 0; padding: 0; box-sizing: border-box; }
  html, body {
    width: 1200px; height: 732px; overflow: hidden;
    background: var(--page-bg);
    font-family: "Arimo", Arial, sans-serif;
  }
  .flyer {
    position: absolute; left: 150px; top: 18px;
    width: 900px; height: 696px; overflow: hidden;
    box-shadow: 0 4px 18px rgba(0,0,0,.25);
  }
  .flyer-art { position: absolute; inset: 0; width: 900px; height: 696px; }
  .headline {
    position: absolute; left: 70px; top: 38px;
    color: var(--ink-green); font-weight: 700; font-size: 25px; line-height: 31px;
    letter-spacing: .2px;
  }
  .headline span { display: block; }
  .headline .line-two { padding-left: 28px; }
  .mail-box {
    position: absolute; left: 652px; top: 14px; width: 236px; height: 150px;
    background: linear-gradient(180deg, var(--paper) 0%, var(--leaf-pale) 100%);
    border-radius: 10px 10px 10px 60px;
    opacity: .94;
  }
  .mail-box .postal-label {
    position: absolute; left: 0; right: 0; bottom: 12px; text-align: center;
    font-size: 13px; font-weight: 700; color: var(--ink-dark);
  }
  .company {
    position: absolute; left: 76px; top: 498px;
  }
  .company-name {
    color: var(--paper); font-size: 38px; font-weight: 700; font-style: italic;
    text-shadow: 0 2px 3px rgba(30,60,5,.45);
  }
  .company-web {
    margin-top: 4px; padding-left: 28px;
    color: var(--paper); font-size: 16px; font-style: italic;
  }
  .contact-card {
    position: absolute; left: 660px; top: 488px; width: 200px; height: 104px;
    background: var(--card); border-radius: 16px;
    text-align: center; padding-top: 18px;
  }
  .contact-cta { color: var(--ink-green); font-size: 20px; }
  .contact-phone { margin-top: 12px; color: var(--ink-dark); font-size: 25px; font-weight: 700; }
</style>
</head>
<body>
  <main class="flyer">
    <svg class="flyer-art" viewBox="0 0 900 696" xmlns="http://www.w3.org/2000/svg">
      <defs>
        <linearGradient id="top-wash" x1="0" y1="0" x2="0" y2="1">
          <stop offset="0" stop-color="#f2f7dc"/>
          <stop offset=".55" stop-color="#d6e79c"/>
          <stop offset="1" stop-color="#a8cb55"/>
        </linearGradient>
        <linearGradient id="base-green" x1="0" y1="0" x2="1" y2="1">
          <stop offset="0" stop-color="#8bb532"/>
          <stop offset="1" stop-color="#5f8c1a"/>
        </linearGradient>
        <linearGradient id="patio-tones" x1="0" y1="0" x2="1" y2="1">
          <stop offset="0" stop-color="#2e3a2a"/>
          <stop offset=".45" stop-color="#8c7a5c"/>
          <stop offset="1" stop-color="#c9b48a"/>
        </linearGradient>
        <linearGradient id="firepit-tones" x1="0" y1="0" x2="1" y2="1">
          <stop offset="0" stop-color="#3d4a2c"/>
          <stop offset="1" stop-color="#9d8f74"/>
        </linearGradient>
        <linearGradient id="pool-tones" x1="0" y1="0" x2="1" y2="1">
          <stop offset="0" stop-color="#5f7d8e"/>
          <stop offset=".5" stop-color="#6c8a4a"/>
          <stop offset="1" stop-color="#b9c6cf"/>
        </linearGradient>
        <clipPath id="photo-clip">
          <path d="M0 130 H900 V380 C700 420 400 440 0 470 Z"/>
        </clipPath>
      </defs>

      <rect class="top-wash" width="900" height="696" fill="url(#top-wash)"/>

      <g class="photo-grid" clip-path="url(#photo-clip)">
        <rect x="70" y="132" width="250" height="160" fill="url(#firepit-tones)" stroke="#fff" stroke-width="4"
              role="img" aria-label="Photo: paver patio with lounge chairs around a fire pit at dusk"/>
        <rect x="70" y="296" width="250" height="190" fill="url(#pool-tones)" stroke="#fff" stroke-width="4"
              role="img" aria-label="Photo: modern home with paver pool deck and landscaped garden"/>
        <path d="M330 132 H900 V480 H330 C360 380 360 230 330 132 Z" fill="url(#patio-tones)" stroke="#fff" stroke-width="5"
              role="img" aria-label="Photo: curved stone paver terrace with outdoor fireplace and dining set at night"/>
      </g>

      <path class="swoosh-white" d="M0 470 C400 440 700 420 900 380 V400 C700 440 400 462 0 490 Z" fill="#ffffff" opacity=".9"/>
      <path class="swoosh-lime" d="M0 488 C400 460 700 438 900 398 V430 C700 470 400 490 0 510 Z" fill="var(--leaf-lime)"/>
      <path class="base-band" d="M0 505 C400 486 700 466 900 426 V696 H0 Z" fill="url(#base-green)"/>
      <path class="base-sheen" d="M0 505 C400 486 700 466 900 426 V450 C700 488 400 505 0 520 Z" fill="#a9cf48" opacity=".6"/>
    </svg>

    <h1 class="headline">
      <span class="line-one">Where the elegance of pavement</span>
      <span class="line-two">Meets the beauty of design..</span>
    </h1>

    <aside class="mail-box">
      <p class="postal-label">Local Postal Customer</p>
    </aside>

    <div class="company">
      <p class="company-name">Evergreen Crest Landscaping</p>
      <p class="company-web">www.evergreencrestpavers.com</p>
    </div>

    <div class="contact-card">
      <p class="contact-cta">contact now!</p>
      <p class="contact-phone">(555) 218-4630</p>
    </div>
  </main>
</body>
</html>
```